Poster design for The Harlowe Co.

Create a poster that will sell our company, all the information needed is on our website @ theharloweco.co.uk
Creative design is down to you.

I have attached the AI for our logo.

```html
<!DOCTYPE html>
<html lang="en">
<head>
<meta charset="utf-8">
<title>The Harlowe Co. — Poster</title>
<link href="https://fonts.googleapis.com/css2?family=Ubuntu:wght@300;400&family=Poiret+One&family=Raleway:wght@100;200&display=swap" rel="stylesheet">
<style>
  :root {
    --paper: #f6f7f7;
    --brand-red: #9b0b0f;
    --ink-grey: #6d6f72;
    --rule-grey: #7a7a7a;
    --word-grey: #c9c9c9;
    --word-pale: #e1e2e2;
    --link-line: #c4c4c4;
    --footer-rule: #b86a55;
    --ink-dark: #2a2a2a;
  }
  * { margin: 0; padding: 0; box-sizing: border-box; }
  html, body { width: 848px; height: 1200px; overflow: hidden; background: var(--paper); }
  .poster { position: relative; width: 848px; height: 1200px; background: var(--paper); overflow: hidden; }

  .brand-mark {
    position: absolute; left: 60px; top: 96px;
    width: 64px; height: 64px; border-radius: 50%;
    background: var(--brand-red);
  }
  .header-divider {
    position: absolute; left: 246px; top: 42px;
    width: 2px; height: 185px; background: var(--rule-grey);
  }
  .company-name {
    position: absolute; left: 276px; top: 80px;
    font-family: "Ubuntu", sans-serif; font-weight: 400;
    font-size: 68px; line-height: 1; color: var(--brand-red); white-space: nowrap;
  }
  .tagline {
    position: absolute; left: 357px; top: 156px;
    font-family: "Ubuntu", sans-serif; font-weight: 300;
    font-size: 23.5px; letter-spacing: 0.2px; color: var(--ink-grey); white-space: nowrap;
  }

  .service-map { position: absolute; left: 0; top: 0; }
  .big-word { font-family: "Raleway", sans-serif; font-weight: 100; fill: var(--word-grey); }
  .big-word--pale { fill: var(--word-pale); }
  .link { stroke: var(--link-line); stroke-width: 1.2; }
  .service-bubble { fill: var(--brand-red); }
  .service-label {
    font-family: "Poiret One", sans-serif; font-weight: 400;
    fill: #ffffff; text-anchor: middle;
  }

  .footer-rule { position: absolute; top: 1102px; height: 1px; background: var(--footer-rule); }
  .footer-rule--left { left: 8px; width: 130px; }
  .footer-rule--right { left: 277px; width: 554px; }
  .footer-name {
    position: absolute; left: 148px; top: 1092px; width: 122px; text-align: center;
    font-family: "Ubuntu", sans-serif; font-weight: 400; font-size: 15px;
    color: var(--brand-red); white-space: nowrap;
  }
  .contact {
    position: absolute; right: 17px; top: 1104px; text-align: right;
    font-family: "Poiret One", sans-serif; font-size: 19px; line-height: 26.5px;
    color: var(--ink-dark); letter-spacing: 0.6px; font-style: normal;
  }
</style>
</head>
<body>
<main class="poster">
  <header>
    <span class="brand-mark" aria-hidden="true"></span>
    <span class="header-divider" aria-hidden="true"></span>
    <h1 class="company-name">The Harlowe Co.</h1>
    <p class="tagline">SIMPLE, SMART AND BEAUTIFUL</p>
  </header>

  <svg class="service-map" width="848" height="1200" viewBox="0 0 842 1191" aria-label="Our services">
    <defs>
      <filter id="bubble-shadow" x="-20%" y="-20%" width="140%" height="140%">
        <feDropShadow dx="2" dy="3" stdDeviation="3" flood-color="#000" flood-opacity="0.35"/>
      </filter>
    </defs>

    <text class="big-word" x="176" y="338" font-size="76">SIMPLE,</text>
    <text class="big-word" x="402" y="518" font-size="142">SMART</text>
    <text class="big-word" x="700" y="790" font-size="172">&amp;</text>
    <text class="big-word big-word--pale" x="14" y="1025" font-size="152">BEAUTIFUL</text>

    <line class="link" x1="124" y1="330" x2="367" y2="399"/>
    <line class="link" x1="367" y1="399" x2="140" y2="532"/>
    <line class="link" x1="140" y1="532" x2="338" y2="652"/>
    <line class="link" x1="338" y1="652" x2="233" y2="811"/>
    <line class="link" x1="233" y1="811" x2="690" y2="582"/>
    <line class="link" x1="690" y1="582" x2="648" y2="857"/>

    <g filter="url(#bubble-shadow)">
      <circle class="service-bubble" cx="124" cy="330" r="56"/>
      <circle class="service-bubble" cx="367" cy="399" r="67"/>
      <circle class="service-bubble" cx="140" cy="532" r="103"/>
      <circle class="service-bubble" cx="338" cy="652" r="68"/>
      <circle class="service-bubble" cx="233" cy="811" r="66"/>
      <circle class="service-bubble" cx="690" cy="582" r="80"/>
      <circle class="service-bubble" cx="648" cy="857" r="82"/>
    </g>

    <text class="service-label" font-size="22"><tspan x="124" y="327">Logo</tspan><tspan x="124" y="354">Design</tspan></text>
    <text class="service-label" font-size="22"><tspan x="367" y="405">Domain</tspan><tspan x="367" y="430">Names</tspan></text>
    <text class="service-label" font-size="23"><tspan x="140" y="524">Domain Linked</tspan><tspan x="140" y="549">Email Accounts</tspan></text>
    <text class="service-label" font-size="27"><tspan x="338" y="648">Website</tspan><tspan x="338" y="674">Design</tspan></text>
    <text class="service-label" font-size="22"><tspan x="233" y="805">Website</tspan><tspan x="233" y="830">Hosting</tspan></text>
    <text class="service-label" font-size="22"><tspan x="690" y="574">Website</tspan><tspan x="690" y="595">Management</tspan></text>
    <text class="service-label" font-size="22"><tspan x="642" y="842">Photography</tspan><tspan x="642" y="867">//</tspan><tspan x="646" y="892">Graphic Stock</tspan></text>
  </svg>

  <footer>
    <span class="footer-rule footer-rule--left" aria-hidden="true"></span>
    <span class="footer-name">The Harlowe Co.</span>
    <span class="footer-rule footer-rule--right" aria-hidden="true"></span>
    <address class="contact">
      http// theharloweco.co.uk<br>
      Tel:&nbsp;&nbsp;&nbsp;07700900417<br>
      Email: info@theharloweco.co.uk
    </address>
  </footer>
</main>
</body>
</html>
```